Brisk Lumo Entertainment

I need a web design for my Business for better online promotions and services.. The name of my company is Brisk Lumo its a entertainment company music, events, networking and so on.. What I do is help artist create and finish projects such as mix tapes, music videos, and book performances in order to create a platform and i also offer representation to help grow there brands or business... I also work with and help develop independent artists!!!

Target Market(s)

Hip hop and R&B industry

Industry/Entity Type

Entertainment Industry

Number of Pages Required

1 page

Requirements
Must have
• Must display My previous and upcoming work i want people to see the quality I provide in my service.. I have more videos that I want to upload on there to show more work.... I would like to bring all the separate promotions and campaigns that I previously had and currently have all one platform for everybody to see and to find more easily instead having everything so spread out..
Nice to have
• Creativity thats going to compliment my work and quality..

```html
<!DOCTYPE html>
<html lang="en">
<head>
<meta charset="utf-8">
<title>Brisk Lumo Entertainment</title>
<link rel="stylesheet" href="https://fonts.googleapis.com/css2?family=Lato:wght@300;400;700;900&family=Quicksand:wght@500;700&family=Roboto+Slab:wght@700&display=swap">
<style>
:root{
  --red:#f0222f;
  --red-deep:#c4161f;
  --black:#0b0b0b;
  --ink:#141414;
  --white:#ffffff;
  --grey:#9b9b9b;
  --card-text:#555555;
  --panel:#8d8d8d;
}
*{margin:0;padding:0;box-sizing:border-box}
html,body{width:1200px;height:2885px;overflow:hidden}
body{position:relative;background:var(--black);font-family:"Lato",sans-serif;color:var(--white)}
.abs{position:absolute}
.backdrop{position:absolute;left:0;top:0;width:1200px;height:2885px}

/* header */
.site-header{left:0;top:0;width:1200px;height:108px;background:linear-gradient(180deg,#5a5a5a,#3a3a3a 60%,#2a2a2a)}
.brand{left:112px;top:0;width:196px;height:108px;background:#151515;display:flex;align-items:center;justify-content:center;gap:10px}
.brand-dot{width:14px;height:14px;background:var(--red)}
.brand-name{font-family:"Lato",sans-serif;font-weight:700;font-size:22px;letter-spacing:1px;color:var(--red)}
.main-nav{left:456px;top:44px;display:flex;font-family:"Roboto Slab",serif;font-weight:700;font-size:17px;letter-spacing:.5px}
.main-nav span{position:absolute;white-space:nowrap}
.search-icon{left:1040px;top:38px}

/* hero */
.hero{left:110px;top:135px;width:967px;height:417px;background:linear-gradient(120deg,#d9d9d9 0%,#8e8e8e 40%,#3b3b3b 75%,#222 100%)}
.hero-title{left:110px;top:338px;width:967px;text-align:center;font-family:"Lato",sans-serif;font-weight:400;font-size:44px;letter-spacing:13px;line-height:52px}

/* welcome */
.section-title{width:1200px;left:0;text-align:center;font-family:"Lato",sans-serif;font-weight:300;font-size:40px}
.welcome-text{left:140px;top:684px;width:914px;text-align:center;font-family:"Quicksand",sans-serif;font-weight:700;font-size:15.5px;line-height:23px}
.read-more{left:523px;top:785px;width:148px;height:39px;border:1.5px solid var(--white);display:flex;align-items:center;justify-content:center;font-size:14px;letter-spacing:1px}

/* work */
.video-card{background:#333;overflow:hidden}
.video-still{position:absolute;left:0;top:0;width:100%;height:calc(100% - 16px)}
.video-label{position:absolute;left:18px;font-family:"Lato",sans-serif;font-weight:900;font-size:18px;letter-spacing:1px}
.video-caption{position:absolute;left:0;width:100%;text-align:center;font-weight:400;font-size:14px;letter-spacing:5px;line-height:17px}
.player-bar{position:absolute;left:0;bottom:0;width:100%;height:16px;background:#f1f1f1}
.player-bar i{position:absolute;top:7px;height:2px;background:#bbb}
.player-bar b{position:absolute;top:5px;width:6px;height:6px;background:#666}
.more-songs{left:477px;top:1513px;display:flex;align-items:center;gap:14px;font-family:"Quicksand",sans-serif;font-weight:700;font-size:17px;letter-spacing:2px;color:var(--red)}

/* team */
.team-panel{left:104px;top:1627px;width:998px;height:598px;background:linear-gradient(180deg,#7c7c7c,#a3a3a3 45%,#6e6e6e);overflow:hidden}
.team-panel .red-edge{position:absolute;left:0;top:0}
.team-title{left:104px;top:1656px;width:998px;text-align:center;font-weight:400;font-size:36px}
.team-rule{left:553px;top:1732px;width:100px;height:1px;background:rgba(255,255,255,.6)}
.member{width:225px;height:423px;top:1771px;background:var(--white)}
.member-photo{width:225px;height:229px;background:linear-gradient(160deg,#dcdccf,#8b8f84 55%,#2e2e2e)}
.member-name{position:absolute;left:19px;top:252px;font-size:16px;color:var(--card-text);letter-spacing:.5px}
.member-name em{font-style:normal;color:var(--red)}
.member-role{position:absolute;left:19px;top:274px;font-size:11px;color:#888}
.member-role.accent{color:var(--red)}
.member-bio{position:absolute;left:19px;top:306px;width:190px;font-family:"Quicksand",sans-serif;font-weight:700;font-size:14px;line-height:25px;color:#9a9a9a}
.member-bio em{font-style:normal;color:var(--red)}

/* event */
.event-title{left:112px;top:2336px;font-family:"Quicksand",sans-serif;font-weight:700;font-size:37px;letter-spacing:.5px}
.event-text{left:112px;top:2408px;width:580px;font-family:"Quicksand",sans-serif;font-weight:700;font-size:17.5px;line-height:28px}
.event-card{left:731px;top:2292px;width:367px;height:323px;background:#fff;box-shadow:0 4px 10px rgba(0,0,0,.3)}
.event-photo{position:absolute;left:6px;top:6px;width:355px;height:285px;background:linear-gradient(170deg,#d6d6d6,#9a9aa2 50%,#4a4a52)}
.event-bar{position:absolute;left:0;bottom:0;width:367px;height:32px;background:var(--red-deep);display:flex;align-items:center;justify-content:space-between;padding:0 16px}
.event-bar span{font-family:"Quicksand",sans-serif;font-weight:700;font-size:19px;letter-spacing:1px}

/* footer */
.site-footer{left:0;top:2662px;width:1200px;height:180px}
.footer-brand{left:171px;top:2702px;width:166px;height:119px;background:#1e1e1e;display:flex;align-items:center;justify-content:center;gap:8px}
.footer-heading{font-family:"Lato",sans-serif;font-weight:700;font-size:32px;letter-spacing:1px}
.footer-links{left:396px;top:2757px;display:grid;grid-template-columns:90px 60px;font-size:14px;font-weight:700;letter-spacing:2px;line-height:21px}
.email-field{left:665px;top:2777px;width:277px;height:44px;background:var(--red);display:flex;align-items:center;padding-left:20px;font-family:"Quicksand",sans-serif;font-weight:700;font-size:15px;letter-spacing:1px}
.subscribe{left:942px;top:2777px;width:137px;height:44px;background:var(--white);color:#111;display:flex;align-items:center;justify-content:center;font-size:19px}
.copyright{left:0;top:2842px;width:1200px;height:43px;background:var(--red);display:flex;align-items:center;justify-content:center;font-family:"Quicksand",sans-serif;font-weight:700;font-size:15px;letter-spacing:1.5px}
</style>
</head>
<body>

<svg class="backdrop" width="1200" height="2885" viewBox="0 0 1200 2885" aria-hidden="true">
  <rect width="1200" height="2885" fill="#0b0b0b"/>
  <rect x="0" y="108" width="1200" height="700" fill="#102014" opacity=".55"/>
  <polygon points="0,808 1200,548 1200,1192 0,1606" fill="#f0222f"/>
  <polygon points="0,808 1200,548 1200,900 0,1100" fill="#9e1a20" opacity=".45"/>
  <polygon points="0,2212 1200,1846 1200,2673 0,2673" fill="#f0222f"/>
</svg>

<header class="abs site-header">
  <div class="abs brand"><span class="brand-dot"></span><span class="brand-name">BRISK LUMO</span></div>
  <nav class="abs main-nav">
    <span style="left:0">HOME</span>
    <span style="left:98px">ABOUT</span>
    <span style="left:209px">GALLERY</span>
    <span style="left:338px">MUSIC</span>
    <span style="left:446px">CONTACT</span>
  </nav>
  <svg class="abs search-icon" width="32" height="32" viewBox="0 0 32 32" aria-hidden="true">
    <circle cx="13" cy="13" r="9" fill="none" stroke="#fff" stroke-width="3"/>
    <line x1="20" y1="20" x2="29" y2="29" stroke="#fff" stroke-width="3.5" stroke-linecap="round"/>
  </svg>
</header>

<div class="abs hero" role="img" aria-label="Black and white photo of the artist standing beside a parked car"></div>
<h1 class="abs hero-title">RIO VANCE<br>THE MONARCH</h1>

<h2 class="abs section-title" style="top:608px">WELCOME</h2>
<p class="abs welcome-text">Lorem ipsum dolor sit amet, consectetur adipisicing elit, sed do eiusmod tempor incididunt ut labore et dolore magna aliqua. Ut enim ad minim veniam, quis nostru. Lorem ipsum dolor sit amet, consectetur adipisicing elit, sed do eiusmod tempor incididunt ut labore et dolore magna aliqua.</p>
<div class="abs read-more">READ MORE</div>

<h2 class="abs section-title" style="top:868px">OUR WORK</h2>

<div class="abs video-card" style="left:104px;top:948px;width:313px;height:263px">
  <div class="video-still" role="img" aria-label="Music video still of a club stage with blue lights" style="background:linear-gradient(135deg,#1a2a8a,#3b56d6 45%,#101030)"></div>
  <div class="player-bar"><b style="left:6px"></b><i style="left:60px;width:150px"></i><i style="left:240px;width:40px;background:#4a7be0"></i></div>
</div>
<div class="abs video-card" style="left:450px;top:948px;width:313px;height:263px">
  <div class="video-still" role="img" aria-label="Album promo still in warm red tones" style="background:linear-gradient(135deg,#5a1a4a,#c2273c 50%,#e35a4a)"></div>
  <div class="video-label" style="top:218px">MY ALBUM</div>
  <div class="player-bar"><b style="left:6px"></b><i style="left:60px;width:150px"></i><i style="left:240px;width:40px;background:#4a7be0"></i></div>
</div>
<div class="abs video-card" style="left:788px;top:948px;width:314px;height:263px">
  <div class="video-still" role="img" aria-label="Album promo still of the artist at night" style="background:linear-gradient(135deg,#2a1208,#6a2a12 50%,#1a0a08)"></div>
  <div class="video-label" style="top:218px">MY ALBUM</div>
  <svg style="position:absolute;left:278px;top:218px" width="22" height="22" viewBox="0 0 22 22" aria-hidden="true"><circle cx="11" cy="11" r="9" fill="none" stroke="#fff" stroke-width="1.6"/><polygon points="9,7 15,11 9,15" fill="#fff"/></svg>
  <div class="player-bar"><b style="left:6px"></b><i style="left:60px;width:150px"></i><i style="left:240px;width:40px;background:#4a7be0"></i></div>
</div>

<div class="abs video-card" style="left:104px;top:1238px;width:313px;height:239px">
  <div class="video-still" role="img" aria-label="Black and white video still of the crew above the artist by a car" style="background:linear-gradient(180deg,#e8e8e8,#7a7a7a 40%,#b8b8b8 55%,#3a3a3a)"></div>
  <div class="video-caption" style="top:162px">RIO VANCE<br>THE MONARCH</div>
  <div class="player-bar"><b style="left:6px"></b><i style="left:30px;width:230px;background:#4a7be0"></i></div>
</div>
<div class="abs video-card" style="left:450px;top:1238px;width:313px;height:239px">
  <div class="video-still" role="img" aria-label="Party flyer still with two men and a red car at night" style="background:linear-gradient(180deg,#1a1a1a,#3a3a3a 30%,#141418 45%,#5a1a22 85%,#1a1a1a)"></div>
  <div class="player-bar"><b style="left:6px"></b><i style="left:60px;width:150px"></i><i style="left:240px;width:40px;background:#4a7be0"></i></div>
</div>
<div class="abs video-card" style="left:788px;top:1238px;width:314px;height:239px">
  <div class="video-still" role="img" aria-label="Black and white video still of the crew above the artist by a car" style="background:linear-gradient(180deg,#e8e8e8,#7a7a7a 40%,#b8b8b8 55%,#3a3a3a)"></div>
  <div class="video-caption" style="top:162px">RIO VANCE<br>THE MONARCH</div>
  <div class="player-bar"><b style="left:6px"></b><i style="left:60px;width:150px"></i><i style="left:240px;width:40px;background:#4a7be0"></i></div>
</div>

<div class="abs more-songs">
  <span>CLICK HERE FOR MORE SONGS</span>
  <svg width="32" height="32" viewBox="0 0 32 32" aria-hidden="true"><circle cx="16" cy="16" r="14" fill="none" stroke="#f0222f" stroke-width="2.4"/><line x1="16" y1="8" x2="16" y2="24" stroke="#f0222f" stroke-width="2.4"/><line x1="8" y1="16" x2="24" y2="16" stroke="#f0222f" stroke-width="2.4"/></svg>
</div>

<section class="abs team-panel" role="img" aria-label="Grey smoke texture behind the team section">
  <svg class="red-edge" width="998" height="598" viewBox="0 0 998 598" aria-hidden="true">
    <polygon points="0,600 998,235 998,598" fill="#f0222f" opacity=".85"/>
  </svg>
</section>
<h2 class="abs team-title">MEET OUR TEAM</h2>
<div class="abs team-rule"></div>

<article class="abs member" style="left:125px">
  <div class="member-photo" role="img" aria-label="Portrait of a bearded team member in a white shirt"></div>
  <div class="member-name">DARNELL BROOKS</div>
  <div class="member-role">CEO</div>
  <p class="member-bio">Lorem ipsum dolor sit amet, consetetur sadipscing elitr, sed diam nonumy eirmod.</p>
</article>
<article class="abs member" style="left:369px">
  <div class="member-photo" role="img" aria-label="Portrait of a team member in a black hat and shirt" style="background:linear-gradient(160deg,#d8d8cc,#5a5a55 55%,#1a1a1a)"></div>
  <div class="member-name">DARNELL BROOKS</div>
  <div class="member-role">CHIEF OFFICER</div>
  <p class="member-bio">Lorem ipsum dolor <em>sit amet, consetetur sadipscing elitr, sed diam nonumy eirmod.</em></p>
</article>
<article class="abs member" style="left:613px">
  <div class="member-photo" role="img" aria-label="Portrait of a team member in sunglasses and a plaid shirt" style="background:linear-gradient(160deg,#cfcfc8,#6a6a6a 50%,#1e3a3a)"></div>
  <div class="member-name">MARCUS <em>HALE</em></div>
  <div class="member-role accent">CREATIVE DIRECTOR</div>
  <p class="member-bio"><em>Lorem ipsum dolor sit amet, consetetur sadipscing elitr, sed diam nonumy eirmod.</em></p>
</article>
<article class="abs member" style="left:858px">
  <div class="member-photo" role="img" aria-label="Portrait of a bearded team member in a white shirt"></div>
  <div class="member-name"><em>NIA CARTER</em></div>
  <div class="member-role accent">CREATIVE DIRECTOR</div>
  <p class="member-bio"><em>Lorem ipsum dolor sit amet, consetetur sadipscing elitr, sed diam nonumy eirmod.</em></p>
</article>

<h2 class="abs event-title">UPCOMING EVENT</h2>
<p class="abs event-text">Lorem ipsum dolor sit amet, consectetur adipisicing elit, sed do eiusmod tempor incididunt ut labore et dolore magna aliqua. Ut enim ad minim veniam, quis nostru.<br>Lorem ipsum dolor sit amet, consectetur adipisicing elit, sed do eiusmod tempor incididunt ut labore et dolore magna aliqua. Ut enim ad minim veniam, quis nostru.</p>
<div class="abs event-card">
  <div class="event-photo" role="img" aria-label="Group photo of three team members standing together"></div>
  <div class="event-bar">
    <span>Events</span>
    <svg width="44" height="18" viewBox="0 0 44 18" aria-hidden="true"><polyline points="12,2 5,9 12,16" fill="none" stroke="#fff" stroke-width="3"/><polyline points="30,2 37,9 30,16" fill="none" stroke="#fff" stroke-width="3"/></svg>
  </div>
</div>

<footer>
  <svg class="abs site-footer" width="1200" height="180" viewBox="0 0 1200 180" aria-hidden="true">
    <path d="M0,11 L12,0 L24,11 L36,0 L48,11 L60,0 L72,11 L84,0 L96,11 L108,0 L120,11 L132,0 L144,11 L156,0 L168,11 L180,0 L192,11 L204,0 L216,11 L228,0 L240,11 L252,0 L264,11 L276,0 L288,11 L300,0 L312,11 L324,0 L336,11 L348,0 L360,11 L372,0 L384,11 L396,0 L408,11 L420,0 L432,11 L444,0 L456,11 L468,0 L480,11 L492,0 L504,11 L516,0 L528,11 L540,0 L552,11 L564,0 L576,11 L588,0 L600,11 L612,0 L624,11 L636,0 L648,11 L660,0 L672,11 L684,0 L696,11 L708,0 L720,11 L732,0 L744,11 L756,0 L768,11 L780,0 L792,11 L804,0 L816,11 L828,0 L840,11 L852,0 L864,11 L876,0 L888,11 L900,0 L912,11 L924,0 L936,11 L948,0 L960,11 L972,0 L984,11 L996,0 L1008,11 L1020,0 L1032,11 L1044,0 L1056,11 L1068,0 L1080,11 L1092,0 L1104,11 L1116,0 L1128,11 L1140,0 L1152,11 L1164,0 L1176,11 L1188,0 L1200,11 L1200,180 L0,180 Z" fill="#111"/>
  </svg>
  <div class="abs footer-brand"><span class="brand-dot"></span><span class="brand-name" style="font-size:19px">BRISK LUMO</span></div>
  <h3 class="abs footer-heading" style="left:394px;top:2708px">NAVIGATION</h3>
  <div class="abs footer-links"><span>HOME</span><span>NEWS</span><span>MUSIC</span><span></span><span>ARTISTE</span></div>
  <h3 class="abs footer-heading" style="left:661px;top:2708px">CONNECT WITH MUSIC</h3>
  <div class="abs email-field">Type your email</div>
  <div class="abs subscribe">Subscribe</div>
  <div class="abs copyright">Copyright 2017 Brisk Lumo.</div>
</footer>

</body>
</html>
```